Personal Injury Billboard for a law frim

Our firm has a billboard we need art for. It will specifically for personal injury cases. The dimensions of art the billboard are 9 ft high 29 feet wide.

We want to highlight the terms, "Serious Injuries" and "Trusted. Local. Experienced." We want to incorporate the attached "Brightvale Honors" badge as well as our attached firm logo. We want the blue color scheme (see attached).

Maybe an image of an industrial plant in the background?

Sans Serif

```html
<!DOCTYPE html>
<html lang="en">
<head>
<meta charset="utf-8">
<title>Serious Injuries Billboard</title>
<link rel="stylesheet" href="https://fonts.googleapis.com/css2?family=Archivo+Black&family=Bebas+Neue&family=Montserrat:wght@700&display=swap">
<style>
  :root {
    --navy-deep: #0b2451;
    --navy: #0c2f6a;
    --navy-light: #1a4a8f;
    --gold: #f5b320;
    --red: #f51505;
  }
  * { margin: 0; padding: 0; box-sizing: border-box; }
  html, body { width: 1200px; height: 415px; overflow: hidden; background: var(--navy-deep); }
  .billboard { position: relative; width: 1200px; height: 415px; overflow: hidden; }
  .plant-scene {
    position: absolute; left: 0; top: 0; width: 1200px; height: 306px;
    background: linear-gradient(180deg, var(--navy) 0%, #0e3776 55%, #14427f 80%, #0f3570 100%);
  }
  .gold-rule { position: absolute; left: 0; top: 306px; width: 1200px; height: 10px; background: var(--gold); }
  .tag-band { position: absolute; left: 0; top: 316px; width: 1200px; height: 99px; background: var(--navy-deep); }
  .headline { position: absolute; left: 0; top: 0; width: 1200px; height: 306px; }
  .headline .serious { font-family: "Bebas Neue", sans-serif; fill: var(--gold); }
  .headline .injuries { font-family: "Archivo Black", sans-serif; fill: var(--red); }
  .tagline { position: absolute; left: 0; top: 316px; width: 1200px; height: 99px; }
  .tagline text { font-family: "Bebas Neue", sans-serif; fill: var(--gold); }
  .honor-name {
    position: absolute; left: 28px; top: 50px; width: 140px;
    font-family: "Montserrat", sans-serif; font-weight: 700; font-size: 24px; line-height: 1.1;
    color: var(--gold); text-align: center; text-transform: uppercase;
  }
  .firm-mark {
    position: absolute; left: 995px; top: 15px; width: 188px; height: 162px;
    background: var(--gold); display: flex; flex-direction: column; align-items: center; justify-content: center;
    font-family: "Montserrat", sans-serif; font-weight: 700; color: var(--navy-deep); text-align: center;
  }
  .firm-mark .firm-name { font-size: 19px; line-height: 1.15; text-transform: uppercase; }
  .firm-mark .firm-web { font-size: 11px; margin-top: 10px; }
</style>
</head>
<body>
<div class="billboard">
  <div class="plant-scene" role="img" aria-label="Night silhouette of an industrial plant with towers and stacks in deep blue"></div>
  <div class="gold-rule"></div>
  <div class="tag-band"></div>

  <svg class="headline" viewBox="0 0 1200 306" aria-label="Serious Injuries">
    <text class="serious" x="375" y="133" font-size="146" textLength="373" lengthAdjust="spacingAndGlyphs">SERIOUS</text>
    <text class="injuries" x="254" y="268" font-size="155" textLength="701" lengthAdjust="spacingAndGlyphs">INJURIES</text>
  </svg>

  <svg class="tagline" viewBox="0 316 1200 99" aria-label="Trusted. Local. Experienced.">
    <text x="247" y="387" font-size="72" textLength="722" lengthAdjust="spacingAndGlyphs">TRUSTED. LOCAL. EXPERIENCED.</text>
  </svg>

  <div class="honor-name">Brightvale<br>Honors</div>

  <div class="firm-mark">
    <div class="firm-name">Harlow<br>Quint<br>Mercer</div>
    <div class="firm-web">www.hqm-law.com</div>
  </div>
</div>
</body>
</html>
```